New Graphic Design Project / Email signiture and Letterhead

I would like a new SIMPLE but high end quality modern/heavy industrial design for an email Signiture and letter head that incorporates product photos or illustrations of our products to show our customers our range of products and also show our head office in Perth Western Australia and also our Australian and international reseller locations.
in my present email signature you would see that I have other company logos these companies are old partners of ours but some are no longer so I would like to have the option to add and change them if things change in the future.
for ideas Our main products are as follows
Composite Hose
Convoluted hose
Metal expansion joints
Fabric expansion joints
Rubber Expansion joints
Please see our website for ideas and our product photos.
www.dravoline.com.au
if you need any further information please let me know
i have attached our old email signiture for reference.
Mark

Target Market(s)

Oil and Gas / Mining / Petroleum and Chemical Refineries, high end engineering

Requirements
Must have
• pictures / photos of our core products and our company capabilities to show our existing and new customers what we can do.
in the email signature - links to company face book and Worklink, our website
I would like to have spaces for my company partners logos and need the final file to be in a format for me to change and update all details
All so our Font is Conthrax SB
Nice to have
• the email signature, I would like this to have all the required information ( as per attached present email signature ) but also be informative / marketing to show customers what we do if possible.
the letter head can be based from the same but simple with or without product photos

```html
<!DOCTYPE html>
<html lang="en">
<head>
<meta charset="utf-8">
<title>Dravoline Email Signature</title>
<link href="https://fonts.googleapis.com/css2?family=Poppins:wght@400;500&display=swap" rel="stylesheet">
<style>
  :root {
    --ink: #1a1a1a;
    --muted: #555555;
    --rule: #cfcfcf;
    --paper: #ffffff;
    --band: #0d0d0d;
    --band-grey: #6b6b6b;
    --stage: #e9e9e9;
    --badge: #c9cdd3;
  }
  * { margin: 0; padding: 0; box-sizing: border-box; }
  html, body { width: 1200px; height: 786px; overflow: hidden; }
  body {
    background: var(--stage);
    font-family: "Poppins", Arial, sans-serif;
    color: var(--ink);
    position: relative;
  }
  .signature {
    position: absolute;
    left: 20px; top: 133px;
    width: 1160px; height: 520px;
    background: var(--paper);
    overflow: hidden;
    box-shadow: 0 6px 20px rgba(0,0,0,.18);
  }
  .swoosh { position: absolute; inset: 0; width: 100%; height: 100%; }

  .brand { position: absolute; left: 24px; top: 118px; display: flex; align-items: center; gap: 8px; }
  .brand-dot { width: 26px; height: 26px; border-radius: 50%; background: var(--muted); }
  .brand-name { font-size: 17px; font-weight: 500; color: var(--muted); letter-spacing: 1px; }

  .person { position: absolute; left: 190px; top: 96px; }
  .person-name { font-size: 26px; font-weight: 400; line-height: 1.1; }
  .person-role { font-size: 21px; font-weight: 400; line-height: 1.2; }

  .divider { position: absolute; top: 36px; width: 1px; height: 78px; background: var(--rule); }

  .contact { position: absolute; display: flex; gap: 10px; font-size: 18px; line-height: 1.25; }
  .contact svg { flex: none; width: 24px; height: 24px; margin-top: 2px; }
  .address { left: 420px; top: 40px; }
  .phones { left: 650px; top: 42px; flex-direction: column; gap: 8px; }
  .phones .line { display: flex; gap: 10px; align-items: center; }
  .web { left: 880px; top: 30px; flex-direction: column; gap: 10px; }
  .web .line { display: flex; gap: 10px; align-items: center; }
  .socials { display: flex; gap: 10px; font-size: 12px; color: var(--muted); }

  .products { position: absolute; left: 210px; top: 172px; display: flex; gap: 14px; }
  .product { width: 172px; text-align: center; }
  .product-photo { width: 172px; height: 136px; border: 1px solid var(--rule); padding: 8px; background: var(--paper); }
  .product-photo div { width: 100%; height: 100%; }
  .product-name { font-size: 14px; margin-top: 6px; white-space: nowrap; }
  .composite { background: linear-gradient(135deg, #2f5d9a, #6f94c4 50%, #bfc4ca); }
  .convoluted { background: linear-gradient(135deg, #d9dde1, #8e959c 50%, #eef0f2); }
  .fabric { background: linear-gradient(135deg, #6f9a55, #a7c58f 50%, #9aa0a6); }
  .rubber { background: linear-gradient(135deg, #c6cbd0, #1a1a1a 50%, #c6cbd0); }
  .metal { background: linear-gradient(135deg, #e4e6e8, #9da3a8 50%, #d7d9db); }

  .partner { position: absolute; background: var(--badge); border-radius: 4px; }

  .regions {
    position: absolute; right: 170px; top: 482px;
    display: flex; align-items: center; gap: 12px;
    color: var(--paper); font-size: 18px;
  }
  .regions svg { width: 16px; height: 20px; }
</style>
</head>
<body>
<main class="signature">
  <svg class="swoosh" viewBox="0 0 1160 520" preserveAspectRatio="none" aria-hidden="true">
    <path d="M0,380 C40,460 140,478 320,476 C620,472 900,420 1160,385 L1160,520 L0,520 Z" fill="var(--band-grey)"/>
    <path d="M0,394 C44,472 146,490 326,488 C626,484 906,434 1160,400 L1160,520 L0,520 Z" fill="var(--paper)"/>
    <path d="M0,402 C48,480 150,498 330,496 C630,492 910,442 1160,410 L1160,520 L0,520 Z" fill="var(--band)"/>
  </svg>

  <div class="brand">
    <span class="brand-dot"></span>
    <span class="brand-name">DRAVOLINE</span>
  </div>

  <div class="person">
    <p class="person-name">Mark Tolland</p>
    <p class="person-role">Managing Director</p>
  </div>

  <span class="divider" style="left:400px"></span>
  <div class="contact address">
    <svg viewBox="0 0 24 24" aria-hidden="true"><path d="M3 21V10l9-6 9 6v11z" fill="none" stroke="var(--ink)" stroke-width="2"/><path d="M7 13h10M7 17h10" stroke="var(--ink)" stroke-width="2"/></svg>
    <p>42 Ferrous Way<br>Harlow Vale<br>WA 6190</p>
  </div>

  <span class="divider" style="left:630px"></span>
  <div class="contact phones">
    <div class="line"><svg viewBox="0 0 24 24" aria-hidden="true"><circle cx="12" cy="12" r="10" fill="none" stroke="var(--ink)" stroke-width="1.6"/><path d="M9 7c-1 2 0 6 4 9l2-2" fill="none" stroke="var(--ink)" stroke-width="2"/></svg><span>+ 614 10 555 218</span></div>
    <div class="line"><svg viewBox="0 0 24 24" aria-hidden="true"><circle cx="12" cy="12" r="10" fill="none" stroke="var(--ink)" stroke-width="1.6"/><path d="M9 7c-1 2 0 6 4 9l2-2" fill="none" stroke="var(--ink)" stroke-width="2"/></svg><span>+ 618 955 50 146</span></div>
  </div>

  <span class="divider" style="left:860px"></span>
  <div class="contact web">
    <div class="line"><svg viewBox="0 0 24 24" aria-hidden="true"><circle cx="12" cy="12" r="10" fill="none" stroke="var(--ink)" stroke-width="1.6"/><path d="M2 12h20M12 2c4 4 4 16 0 20M12 2c-4 4-4 16 0 20" fill="none" stroke="var(--ink)" stroke-width="1.4"/></svg><span>www.dravoline.com.au</span></div>
    <div class="socials"><span>Snapgrid</span><span>Friendwall</span><span>Worklink</span><span>Chatline</span></div>
  </div>

  <section class="products">
    <figure class="product"><div class="product-photo"><div class="composite" role="img" aria-label="Photo of coiled blue composite hose with flanged ends"></div></div><figcaption class="product-name">Composite Hose</figcaption></figure>
    <figure class="product"><div class="product-photo"><div class="convoluted" role="img" aria-label="Photo of coiled stainless convoluted hose"></div></div><figcaption class="product-name">Convoluted Hose</figcaption></figure>
    <figure class="product"><div class="product-photo"><div class="fabric" role="img" aria-label="Photo of green framed fabric expansion joints"></div></div><figcaption class="product-name">Fabric Expansion Joints</figcaption></figure>
    <figure class="product"><div class="product-photo"><div class="rubber" role="img" aria-label="Photo of black rubber expansion joint between steel flanges"></div></div><figcaption class="product-name">Rubber Expansion Joints</figcaption></figure>
    <figure class="product"><div class="product-photo"><div class="metal" role="img" aria-label="Photo of assorted metal bellows expansion joints"></div></div><figcaption class="product-name">Metal Expansion Joints</figcaption></figure>
  </section>

  <span class="partner" style="left:160px; top:420px; width:140px; height:24px"></span>
  <span class="partner" style="left:330px; top:404px; width:96px; height:32px"></span>
  <span class="partner" style="left:460px; top:390px; width:42px; height:40px; border-radius:50%"></span>
  <span class="partner" style="left:545px; top:380px; width:60px; height:34px"></span>
  <span class="partner" style="left:645px; top:370px; width:66px; height:30px"></span>
  <span class="partner" style="left:760px; top:360px; width:84px; height:30px"></span>
  <span class="partner" style="left:880px; top:348px; width:38px; height:38px; border-radius:50%"></span>
  <span class="partner" style="left:960px; top:346px; width:120px; height:28px"></span>

  <div class="regions">
    <svg viewBox="0 0 16 20" aria-hidden="true"><path d="M8 0a7 7 0 0 0-7 7c0 5 7 13 7 13s7-8 7-13a7 7 0 0 0-7-7z" fill="var(--paper)"/><circle cx="8" cy="7" r="2.6" fill="var(--band)"/></svg>
    <span>Australia, Singapore, Indonesia, Vietnam</span>
  </div>
</main>
</body>
</html>
```